Milkman leaflet

We are looking for a flyer designed to target new customers. The main benefit that needs highliting is the fact that farmers get more per litre by buying from us than from the larger milk processors.
We are looking for a traditional design which takes readers back to the good old days before supermarkets started destroying small businesses.

Target Market(s)

Families and retired people

Requirements
Must have
• The flyer will be designed as an A5 document with two sides.
At least three pictures
The company logo
Tel: 0121 496 0735
www.pwdairies.co.uk

```html
<!DOCTYPE html>
<html lang="en">
<head>
<meta charset="utf-8">
<title>Parkwood Dairies – Milkman Leaflet</title>
<link href="https://fonts.googleapis.com/css2?family=Lobster&family=Questrial&family=Arimo:wght@700&display=swap" rel="stylesheet">
<style>
  :root{
    --blue:#1e6fb4;
    --blue-dark:#0f4f8e;
    --blue-light:#3f90d0;
    --card:#e6e8f2;
    --white:#ffffff;
    --ink:#1c1c1c;
    --red:#e8412a;
    --green:#4aa326;
    --sky-top:#6fb3ea;
    --sky-low:#d7ecfa;
    --grass:#5fae2c;
    --grass-dark:#3f8a1a;
  }
  *{margin:0;padding:0;box-sizing:border-box}
  html,body{width:846px;height:1200px;overflow:hidden;background:#fff}
  .leaflet{
    position:relative;width:846px;height:1200px;overflow:hidden;
    background:radial-gradient(circle at 50% 60%, var(--blue-light) 0%, var(--blue) 45%, var(--blue-dark) 100%);
    font-family:"Questrial", "Century Gothic", sans-serif;color:var(--ink);
  }
  .hero-photo{
    position:absolute;left:17px;top:17px;width:812px;height:437px;
    background:linear-gradient(180deg,var(--sky-top) 0%,var(--sky-low) 55%,var(--grass) 72%,var(--grass-dark) 100%);
  }
  .intro-box{
    position:absolute;left:34px;top:34px;width:363px;height:235px;
    background:var(--white);padding:10px 12px;
    box-shadow:2px 3px 6px rgba(0,0,0,.25);
  }
  .heading{font-family:"Lobster", cursive;font-weight:400;line-height:1.05}
  .intro-box .heading{color:var(--green);font-size:25px;margin-bottom:2px}
  .body-text{font-size:20.5px;line-height:26.6px}
  .slogan{
    position:absolute;left:27px;top:436px;width:562px;height:120px;
    background:var(--white);transform:rotate(-3deg);
    box-shadow:2px 4px 8px rgba(0,0,0,.3);
    display:flex;flex-direction:column;justify-content:center;padding-left:22px;
  }
  .slogan .heading{color:var(--blue);font-size:40px;line-height:1.12;white-space:nowrap}
  .slogan .heading:first-child{padding-left:96px}
  .card{
    position:absolute;background:var(--card);padding:10px 12px;
    box-shadow:2px 3px 6px rgba(0,0,0,.25);
  }
  .card .heading{color:var(--red);font-size:25px;margin-bottom:2px;white-space:nowrap}
  .card-doorstep{left:17px;top:595px;width:264px;height:494px}
  .card-community{left:312px;top:595px;width:276px;height:494px}
  .card-farmers{left:615px;top:489px;width:214px;height:606px}
  .card-farmers .body-text{font-size:20px}
  .card-photo{position:absolute;left:12px;right:12px;bottom:2px}
  .photo-bottles{height:150px;background:linear-gradient(180deg,#6d6b5e 0%,#ecece6 45%,#4b4a40 100%)}
  .photo-house{height:120px;background:linear-gradient(180deg,#c9d9e8 0%,#9a5a40 45%,#3f6b2e 100%)}
  .buy-local-badge{
    position:absolute;left:12px;bottom:20px;width:184px;height:55px;
    background:var(--white);border:2px solid var(--blue-dark);
  }
  .footer{position:absolute;left:0;top:1080px;width:846px;height:120px}
  .footer svg{position:absolute;inset:0}
  .brand{
    position:absolute;left:17px;top:1125px;width:172px;height:66px;
    display:flex;align-items:center;gap:8px;padding:0 6px;background:var(--white);
    font-family:"Arimo", Arial, sans-serif;font-weight:700;font-size:21px;line-height:1.05;color:var(--blue-dark);
  }
  .brand-mark{flex:none;width:30px;height:30px;border-radius:50%;background:var(--blue-dark)}
  .contact{
    position:absolute;left:213px;top:1149px;white-space:nowrap;
    font-family:"Arimo", Arial, sans-serif;font-weight:700;font-size:30.5px;line-height:1;color:var(--blue-dark);
  }
</style>
</head>
<body>
<main class="leaflet">
  <div class="hero-photo" role="img" aria-label="Glass jugs and bottles of milk standing on green grass with white daisies under a blue sky"></div>

  <section class="intro-box">
    <h2 class="heading">Home milk delivery is “green”</h2>
    <p class="body-text">It is nice to know that when you buy milk from the milkman you are doing your bit towards the environment as well. Milk delivered to your door comes in glass bottles which are reusable and recyclable, saving energy and resources.</p>
  </section>

  <div class="slogan">
    <p class="heading">Keep it British!</p>
    <p class="heading">Support your local milkman.</p>
  </div>

  <section class="card card-doorstep">
    <h3 class="heading">Milk delivered fresh<br>to your doorstep</h3>
    <p class="body-text">A regular milk delivery means you never have to worry about queuing up in shops or running out of milk for your morning cuppa or breakfast cereals and you can be confident your milk is fresh when it arrives.</p>
    <div class="card-photo photo-bottles" role="img" aria-label="Three glass milk bottles on a stone doorstep"></div>
  </section>

  <section class="card card-community">
    <h3 class="heading">The milkman keeps an<br>eye on the community</h3>
    <p class="body-text">Helping our customers is simply part of the job for our milkmen, many of whom have foiled burglars, spotted house fires or helped people who are injured or ill. It is also reassuring to know that there is always someone keeping an eye on your house while you are away.</p>
    <div class="card-photo photo-house" role="img" aria-label="Red brick family house with a front lawn"></div>
  </section>

  <section class="card card-farmers">
    <h3 class="heading">Fair pay<br>for the farmers</h3>
    <p class="body-text">It is reassuring for many customers that all of the farmers who supply our milk are paid a premium above what the larger dairies are paying. If the supermarkets get their way there will eventually be no milk production in the UK and all milk will be imported. We certainly hope this never happens!</p>
    <div class="buy-local-badge" role="img" aria-label="Buy British badge"></div>
  </section>

  <footer class="footer">
    <svg width="846" height="120" viewBox="0 0 846 120" aria-hidden="true">
      <path d="M0 28 C60 10 110 40 180 22 C260 2 320 36 420 20 C520 6 600 34 700 18 C770 8 820 26 846 20 L846 120 L0 120 Z" fill="#ffffff"/>
    </svg>
  </footer>
  <div class="brand"><span class="brand-mark"></span><span>Parkwood<br>Dairies</span></div>
  <p class="contact">Tel: 0121 496 0735 • www.pwdairies.co.uk</p>
</main>
</body>
</html>
```